Motivational Poster Series for Students at Truck Driving School

We are looking for a series of 3 motivational posters (18"X 24") to be used in classrooms at a truck driving school. The audience for the posters will be the students that are currently in school and the purpose of the posters is to be motivational pieces that will be displayed on the walls.

We have provided the quotes below that are to be used on each poster. We have also provided some example images from PixVaultImages to give an idea on the backgrounds that we'd like to see on each poster. The images do not have to be exact, these are just examples of what we think will look good for each quote. Since this is a series, they can all be somewhat similar in look/feel - just with different images and quotes.

So, the basic idea is a background image/design with a quote being the main point of emphasis. Other than that, we would like to include the logo provided at a small scale in one of the corners of the poster as a watermark for branding purposes.

Below are the quotes for each of the 3 posters:

Poster 1 - “It’s very difficult to follow our dreams, but it’s even more difficult to forget them.” - Devan Okafor

Poster 2 - “Success doesn’t just come and find you, you have to go out and get it.” - Unknown

Poster 3 - “If you are not willing to learn, no one can help you. If you are determined to learn, no one can stop you.”
- Unknown

NOTE: these posters should be designed as 18" X 24" in size with 2 of them being landscape and one being portrait orientation (as shown in images provided below)

Below are some sample images to give an idea on what could be used as background design for each quote. The logo that should be used as a watermark in a corner for some subtle branding has been provided as well.

Target Market(s)

The target market for this series are truck drivers between the ages of 25-55. Mostly males.

Industry/Entity Type

Landscape

Requirements
Must have
• Quote featured, high quality background design/image, logo watermark

```html
<!DOCTYPE html>
<html lang="en">
<head>
<meta charset="utf-8">
<title>Follow Our Dreams — Motivational Poster</title>
<link rel="stylesheet" href="https://fonts.googleapis.com/css2?family=Barlow+Condensed:wght@300;400;700&display=swap">
<style>
  :root {
    --sky-top: #4e6f9c;
    --sky-mid: #7b98bb;
    --sky-low: #a9b8c6;
    --hills: #5b606b;
    --desert-light: #8a7359;
    --desert: #6e5a46;
    --desert-dark: #4d4138;
    --road: #2d2e31;
    --road-deep: #1f2023;
    --accent-red: #d0302f;
    --wash: rgba(242, 240, 236, 0.72);
    --quote-white: #ffffff;
    --brand-ink: #1c1c1c;
  }
  html, body {
    margin: 0;
    padding: 0;
    overflow: hidden;
    background: #ffffff;
  }
  .poster {
    position: relative;
    width: 1200px;
    height: 900px;
    overflow: hidden;
    font-family: "Barlow Condensed", "Arial Narrow", sans-serif;
  }
  .poster__backdrop {
    position: absolute;
    inset: 0;
    background:
      radial-gradient(ellipse 260px 520px at 580px 900px, rgba(20,20,22,0.55), rgba(20,20,22,0) 70%),
      linear-gradient(180deg,
        var(--sky-top) 0%,
        var(--sky-mid) 24%,
        var(--sky-low) 38%,
        #b8c0c6 41%,
        var(--hills) 42.5%,
        #6a655e 44.5%,
        var(--desert-light) 47%,
        var(--desert) 54%,
        var(--desert-dark) 62%,
        var(--road) 74%,
        var(--road-deep) 100%);
  }
  .poster__frame {
    position: absolute;
    inset: 0;
  }
  .quote {
    position: absolute;
    left: 12px;
    top: 89px;
    width: 680px;
    margin: 0;
    text-align: center;
    color: var(--quote-white);
    line-height: 62px;
    text-shadow: 0 1px 3px rgba(0,0,0,0.25);
  }
  .quote__line {
    display: block;
    white-space: nowrap;
  }
  .quote__line--light {
    font-weight: 300;
    font-size: 68px;
  }
  .quote__line--strong {
    font-weight: 700;
    font-size: 66px;
    letter-spacing: 0.3px;
  }
  .quote__author {
    display: block;
    font-style: normal;
    font-weight: 300;
    font-size: 66px;
    white-space: nowrap;
  }
  .brand {
    position: absolute;
    right: 28px;
    bottom: 40px;
    display: flex;
    align-items: center;
    gap: 12px;
    color: var(--brand-ink);
    font-weight: 700;
    font-size: 30px;
    letter-spacing: 0.5px;
  }
  .brand__mark {
    width: 22px;
    height: 22px;
    background: var(--accent-red);
  }
</style>
</head>
<body>
  <main class="poster">
    <div class="poster__backdrop" role="img" aria-label="Photograph of an empty desert highway stretching straight to distant mountains under a blue sky"></div>

    <svg class="poster__frame" width="1200" height="900" viewBox="0 0 1200 900" aria-hidden="true">
      <path class="frame__wash" fill="var(--wash)"
            d="M440,900 C760,780 1070,470 1200,40 L1200,900 Z"/>
      <path class="frame__swoosh" fill="var(--accent-red)"
            d="M380,900 C700,760 1040,460 1188,0 L1200,0 L1200,40 C1070,470 760,780 440,900 Z"/>
    </svg>

    <blockquote class="quote">
      <span class="quote__line quote__line--light">It’s very difficult to</span>
      <span class="quote__line quote__line--strong">FOLLOW OUR DREAMS,</span>
      <span class="quote__line quote__line--light">but it’s even more</span>
      <span class="quote__line quote__line--strong">DIFFICULT TO FORGET THEM.</span>
      <cite class="quote__author">— Devan Okafor —</cite>
    </blockquote>

    <div class="brand">
      <span class="brand__mark"></span>
      <span class="brand__name">Mileline Driver School</span>
    </div>
  </main>
</body>
</html>
```